Website design for recruitment solutions

We connect top talents to fast growing employers in Asia. We need to revamp our existing website (currently outdated) and also add more pages to make it more informative for talents and employers.
We need final design output to be for both desktop and mobile devices. The final design output must come with all specifications so it's easier for our dev team to implement. We have a detailed mockup but we expect the design to be significantly changed by the final output. We want the pages to look aesthetic, modern and professional.
Number of Pages Required
5+ page
Requirements
Must have
- - To have Pages design for desktop+mobile. Need to take into account intermediate resolutions like 1365px\1023px\767px\479px, especially if mobile/desktop design differs considerably. Design should be repeatable (between pages), suitable for block-layout.
Nice to have
- In terms of receiving files, we usually work with designers who can deliver files in Figma or Sketch with export to Figma. If in PSD format - please export to Zeplin or Avocode, otherwise will be difficult to open

```html
<!DOCTYPE html>
<html lang="en">
<head>
<meta charset="utf-8">
<title>TALVEON – Recruitment for Asia</title>
<link href="https://fonts.googleapis.com/css2?family=Montserrat:wght@300;400;500;600;700;900&display=swap" rel="stylesheet">
<style>
:root{
  --nav-green:#6cb28c;
  --feature-top:#d8f2dd;
  --feature-bottom:#ecf7ef;
  --card:#d4efdb;
  --card-mid:#c8ebd5;
  --icon-a:rgba(92,207,108,.30);
  --icon-b:rgba(139,220,155,.22);
  --ink:#222;
  --ink-soft:#333;
  --red:#ff0a0a;
  --testimonial-bg:#dcdddd;
  --testimonial-ink:#5e5e5e;
  --footer-bg:#545554;
  --white:#fff;
}
*{margin:0;padding:0;box-sizing:border-box}
html,body{width:1200px;height:2250px;overflow:hidden}
body{position:relative;font-family:'Montserrat',sans-serif;color:var(--ink);background:var(--footer-bg)}

/* Navigation */
.site-nav{position:absolute;left:0;top:0;width:1200px;height:74px;background:var(--nav-green);z-index:3}
.brand{position:absolute;left:148px;top:22px;font-weight:700;font-size:27px;color:var(--white);letter-spacing:.5px}
.nav-link{position:absolute;top:30px;font-size:11px;font-weight:500;color:var(--white);text-decoration:none}
.nav-link.is-active{color:#5ee27a}
.nav-register{position:absolute;left:890px;top:23px;width:89px;height:29px;border:2px solid var(--red);border-radius:5px;color:var(--red);font-size:11px;font-weight:500;display:flex;align-items:center;justify-content:center}

/* Hero */
.hero{position:absolute;left:0;top:74px;width:1200px;height:487px;background:linear-gradient(160deg,#c4eace 0%,#b2e4c6 55%,#c2ead3 100%);overflow:hidden}
.hero-art{position:absolute;left:15px;top:16px;width:1090px;height:400px;border-radius:0 0 50% 50%/0 0 40px 40px;background:radial-gradient(ellipse at 50% 70%,rgba(190,214,160,.55) 0%,rgba(150,196,170,.35) 55%,rgba(184,230,203,0) 80%)}
.hero-title{position:absolute;left:0;top:104px;width:1200px;text-align:center;font-weight:900;font-size:53px;line-height:63px;color:var(--ink)}
.btn-start{position:absolute;left:506px;top:307px;width:187px;height:49px;border-radius:25px;background:var(--red);color:var(--white);font-weight:700;font-size:23px;display:flex;align-items:center;justify-content:center}
.learn-more{position:absolute;left:0;top:437px;width:1200px;text-align:center;font-size:13px;font-weight:600;color:var(--ink)}

/* Features */
.features{position:absolute;left:0;top:561px;width:1200px;height:807px;background:linear-gradient(180deg,var(--feature-top),var(--feature-bottom))}
.feature-card{position:absolute;background:var(--card)}
.feature-card h2{font-weight:400;font-size:23px;margin-bottom:12px;color:var(--ink)}
.feature-card p{font-size:13.6px;line-height:27px;color:var(--ink-soft)}
.card-smart{left:148px;top:76px;width:300px;height:356px;padding:32px 24px 32px 38px}
.card-people{left:748px;top:76px;width:300px;height:356px;padding:32px 38px 32px 24px;text-align:right}
.card-insights{left:449px;top:376px;width:299px;height:356px;background:var(--card-mid);padding:32px 14px 32px 36px}
.feature-icon{position:absolute;border-radius:12px;background:linear-gradient(135deg,var(--icon-a),var(--icon-b))}
.icon-signpost{left:485px;top:151px;width:226px;height:225px}
.icon-network{left:186px;top:356px;width:224px;height:228px}
.icon-group{left:786px;top:356px;width:224px;height:228px}

/* Testimonials */
.testimonials{position:absolute;left:0;top:1368px;width:1200px;height:340px;background:var(--testimonial-bg)}
.testimonials h2{position:absolute;left:0;top:30px;width:1200px;text-align:center;font-weight:400;font-size:38px;letter-spacing:2px;color:var(--testimonial-ink)}
.wave{position:absolute;left:0;top:1700px;width:1200px;height:90px}

/* Footer */
.footer-brand{position:absolute;left:148px;top:1825px;font-weight:300;font-size:37px;color:var(--white);letter-spacing:.5px}
.footer-about{position:absolute;left:149px;top:1893px;width:180px;font-size:14px;line-height:16px;color:var(--white)}
.footer-heading{position:absolute;top:1835px;font-weight:400;font-size:23px;color:var(--white)}
.footer-links{position:absolute;top:1891px;list-style:none;font-size:13.5px;line-height:22px;color:var(--white)}
.footer-register{position:absolute;left:416px;top:1966px;width:89px;height:29px;border:2px solid var(--red);border-radius:5px;color:var(--red);font-size:10px;display:flex;align-items:center;justify-content:center}
.social{position:absolute;top:2088px;width:38px;height:38px;border-radius:50%;background:#111}
.legal{position:absolute;top:2163px;font-size:10.5px;font-weight:700;line-height:12.5px;color:var(--white);white-space:nowrap}
</style>
</head>
<body>

<header class="site-nav">
  <div class="brand">TALVEON</div>
  <a class="nav-link" style="left:448px">HOW WE WORK</a>
  <a class="nav-link is-active" style="left:574px">BROWSE JOBS</a>
  <a class="nav-link" style="left:691px">EMPLOYERS</a>
  <a class="nav-link" style="left:795px">ABOUT US</a>
  <div class="nav-register">REGISTER</div>
  <a class="nav-link" style="left:1015px">LOGIN</a>
</header>

<section class="hero">
  <div class="hero-art" role="img" aria-label="Illustration of professionals walking out of a large phone screen onto a platform"></div>
  <h1 class="hero-title">We connect top talents into<br>fast growing employers in Asia</h1>
  <div class="btn-start">Get Started</div>
  <div class="learn-more">Learn more</div>
</section>

<section class="features">
  <div class="feature-card card-smart">
    <h2>Smart connections</h2>
    <p>It's the quality of the connection that matters. Our role matching algorithms and talent managers work around the clock to find opportunities suitable to your unique profile.</p>
  </div>
  <div class="feature-card card-people">
    <h2>People first</h2>
    <p>We take the time to really understand you holistically as a person to maximize your potential. As your career counselor, we provide maximum transparency and feedback throughout the process.</p>
  </div>
  <div class="feature-card card-insights">
    <h2>Critical insights</h2>
    <p>Our close interactions with candidates and employers have helped us create a comprehensive database of companies, talents and skills. With TALVEON, you will gain full access to timely intel to help you make the right career decision.</p>
  </div>

  <div class="feature-icon icon-signpost" role="img" aria-label="Green line illustration of a signpost with arrows pointing both ways"></div>
  <div class="feature-icon icon-network" role="img" aria-label="Green line illustration of connected people in a network"></div>
  <div class="feature-icon icon-group" role="img" aria-label="Green line illustration of a group of standing people"></div>
</section>

<section class="testimonials">
  <h2>Testimonials</h2>
</section>
<svg class="wave" viewBox="0 0 1200 90" preserveAspectRatio="none">
  <path d="M0 0 H1200 V78 Q1170 84 1140 76 Q1000 22 760 24 Q480 28 260 58 Q60 70 0 8 Z" fill="var(--testimonial-bg)"/>
</svg>

<footer>
  <div class="footer-brand">TALVEON</div>
  <p class="footer-about">TALVEON is amodern recruitment partner for high potential techonology and finance talents. We work closely withhedge funds, systematic tradingand FinTecemployers experiencing hyper growth in asia</p>

  <h3 class="footer-heading" style="left:416px">TALENTS</h3>
  <ul class="footer-links" style="left:416px"><li>How We Wok</li><li>Brows Jobs</li></ul>
  <div class="footer-register">REGISTER</div>

  <h3 class="footer-heading" style="left:617px">EMPLOYERS</h3>
  <ul class="footer-links" style="left:620px"><li>Why TALVEON</li></ul>

  <h3 class="footer-heading" style="left:853px">ABOUT US</h3>
  <ul class="footer-links" style="left:854px"><li>About TALVEON</li><li>Working at TALVEON</li></ul>

  <div class="social" style="left:149px" aria-label="Social profile"></div>
  <div class="social" style="left:224px" aria-label="Social profile"></div>

  <p class="legal" style="left:149px;top:2166px">© TALVEON 2012 - 2020 All rights reserved.</p>
  <p class="legal" style="left:400px">Harbourline Talent Limited (EA License No - 40517)<br>Room 12, Level 5, Tower 2 Core B, 88 Harbour Road,<br>Wan Chai, Hong Kong</p>
  <p class="legal" style="left:740px">Talveon Pte, Ltd. (License No - 19K4402)<br>42 Marina Rd, #18 - 02 Bay Center, Singapore 018960</p>
</footer>

</body>
</html>
```